Zielgruppe
Wir sind ein klassisches IT Systemhaus und betreuen in unserer Region kleine und mittelständische Unternehmen sowie öffentliche Einrichtungen.
Aufgabenstellung
Es soll ein modernes Desigm, eine moderne Menüführung vorhanden sein. Dabei soll ein Megamenü eingebunden werden

```html
<!DOCTYPE html>
<html lang="en">
<head>
<meta charset="utf-8">
<title>Norvyn – IT-Solutions</title>
<link href="https://fonts.googleapis.com/css2?family=Work+Sans:wght@500;600;700&family=Open+Sans:wght@400;600&display=swap" rel="stylesheet">
<style>
  :root {
    --ink-dark: #05080b;
    --accent: #25dfe6;
    --white: #ffffff;
    --violet: #5234ea;
    --violet-field: #6056fb;
    --page-light: #f0f1f4;
    --photo-a: #0f2a30;
    --photo-b: #5c7d83;
  }
  * { margin: 0; padding: 0; box-sizing: border-box; }
  html, body { width: 1200px; height: 648px; overflow: hidden; }
  body { position: relative; background: var(--page-light); font-family: "Open Sans", sans-serif; color: var(--white); }

  .hero {
    position: absolute; left: 0; top: 0; width: 1200px; height: 551px;
    background: linear-gradient(90deg, #0b2a30 0%, var(--ink-dark) 22%, var(--ink-dark) 50%, #091416 60%);
  }
  .hero-photo {
    position: absolute; left: 565px; top: 0; width: 635px; height: 551px;
    background: linear-gradient(90deg, rgba(5,8,11,1) 0%, rgba(5,8,11,0) 35%),
                radial-gradient(ellipse at 58% 48%, var(--photo-b) 0%, #2f4d52 40%, var(--photo-a) 75%, #0a1a1e 100%);
  }

  .site-header { position: absolute; left: 0; top: 0; width: 1200px; height: 74px; }
  .brand { position: absolute; left: 170px; top: 23px; display: flex; align-items: center; gap: 7px; }
  .brand-dot { width: 16px; height: 16px; border-radius: 50%; background: var(--accent); }
  .brand-name { font-family: "Work Sans", sans-serif; font-weight: 600; font-size: 22px; color: var(--white); letter-spacing: 0.3px; }

  .main-nav { position: absolute; top: 29px; left: 0; font-family: "Work Sans", sans-serif; font-weight: 500; font-size: 10.5px; }
  .main-nav a { position: absolute; white-space: nowrap; color: var(--white); text-decoration: none; display: flex; align-items: center; gap: 5px; }
  .main-nav a.is-active { color: var(--accent); }
  .main-nav svg { width: 7px; height: 5px; }
  .search-icon { position: absolute; left: 903px; top: 30px; width: 11px; height: 11px; }

  .hero-copy { position: absolute; left: 180px; top: 147px; width: 360px; }
  .eyebrow { font-family: "Work Sans", sans-serif; font-weight: 600; font-size: 10.5px; color: var(--accent); }
  .hero-title { margin-top: 16px; font-family: "Work Sans", sans-serif; font-weight: 700; font-size: 38px; line-height: 44px; }
  .hero-text { margin-top: 22px; font-size: 10.5px; line-height: 17.6px; width: 320px; }
  .btn { display: inline-flex; align-items: center; justify-content: center; font-family: "Work Sans", sans-serif; font-weight: 600; background: var(--accent); color: var(--white); text-decoration: none; }
  .btn-learn { margin-top: 27px; width: 111px; height: 35px; font-size: 10.5px; }

  .appointment {
    position: absolute; left: 170px; top: 466px; width: 744px; height: 182px;
    background: linear-gradient(120deg, var(--violet) 0%, #5a3cf0 55%, var(--violet) 100%);
  }
  .appointment h2 { position: absolute; left: 32px; top: 33px; font-family: "Work Sans", sans-serif; font-weight: 600; font-size: 20px; }
  .appointment .lead { position: absolute; left: 32px; top: 56px; font-size: 10px; color: rgba(255,255,255,0.75); }
  .field { position: absolute; top: 94px; width: 214px; height: 37px; background: var(--violet-field); font-size: 10px; padding-left: 13px; display: flex; align-items: center; color: rgba(255,255,255,0.9); }
  .field-name { left: 32px; }
  .field-email { left: 265px; }
  .field-select { left: 498px; justify-content: space-between; padding-right: 13px; }
  .appointment .note { position: absolute; left: 32px; top: 154px; width: 420px; font-size: 10px; line-height: 15.5px; color: rgba(255,255,255,0.75); white-space: nowrap; }
  .btn-appointment { position: absolute; left: 571px; top: 151px; width: 141px; height: 40px; font-size: 10.5px; }
</style>
</head>
<body>
  <section class="hero">
    <div class="hero-photo" role="img" aria-label="Photo of a thoughtful developer working at a laptop in a dim office with charts on the wall"></div>

    <header class="site-header">
      <div class="brand"><span class="brand-dot"></span><span class="brand-name">norvyn.</span></div>
      <nav class="main-nav">
        <a class="is-active" style="left:457px">Home <svg viewBox="0 0 7 5"><path d="M1 1l2.5 2.5L6 1" fill="none" stroke="currentColor" stroke-width="1.2"/></svg></a>
        <a style="left:530px">About <svg viewBox="0 0 7 5"><path d="M1 1l2.5 2.5L6 1" fill="none" stroke="currentColor" stroke-width="1.2"/></svg></a>
        <a style="left:602px">Services <svg viewBox="0 0 7 5"><path d="M1 1l2.5 2.5L6 1" fill="none" stroke="currentColor" stroke-width="1.2"/></svg></a>
        <a style="left:688px">Pages <svg viewBox="0 0 7 5"><path d="M1 1l2.5 2.5L6 1" fill="none" stroke="currentColor" stroke-width="1.2"/></svg></a>
        <a style="left:760px">News <svg viewBox="0 0 7 5"><path d="M1 1l2.5 2.5L6 1" fill="none" stroke="currentColor" stroke-width="1.2"/></svg></a>
        <a style="left:830px">Contact</a>
      </nav>
      <svg class="search-icon" viewBox="0 0 11 11"><circle cx="4.5" cy="4.5" r="3.3" fill="none" stroke="#fff" stroke-width="1.6"/><path d="M7 7l3 3" stroke="#fff" stroke-width="1.8" stroke-linecap="round"/></svg>
    </header>

    <div class="hero-copy">
      <p class="eyebrow">We Provide IT-Services</p>
      <h1 class="hero-title">Best IT-Solutions<br>near the world</h1>
      <p class="hero-text">Dolor sit amet consectetur elit sed do eiusmod tempor incidi dunt labore et dolore magna.</p>
      <a class="btn btn-learn">Learn more</a>
    </div>
  </section>

  <section class="appointment">
    <h2>Book Appointment</h2>
    <p class="lead">Dolor sit amet consectetur elit sed do eiusmod tempor incididunt</p>
    <div class="field field-name">Your name</div>
    <div class="field field-email">Your email</div>
    <div class="field field-select"><span>---</span><svg width="9" height="6" viewBox="0 0 9 6"><path d="M1 1l3.5 3.5L8 1" fill="none" stroke="#fff" stroke-width="1.4"/></svg></div>
    <p class="note">Lorem ipsum dolor amet constur adipisicing elit sed eiusmpor incid dolore magna<br>aliqu enim minim veniam quis nostrud exercittion.</p>
    <a class="btn btn-appointment">Get Appointment</a>
  </section>
</body>
</html>
```